Re make of the website. A fine diamond jeweller based in Melbourne Australia.

We would like the website redesigned. http://hollisfenwick.com.au/

Current website is very dated and we would like it re made and updated. An example of what we would like is https://www.taryndulcette.com/au/ or https://brindlecove.co.nz/

We sell high end diamond jewellery and the main purpose of the website will be to get people to enquire and make a booking to design a ring/meet with the experts in store. There is also a small online store.

Target Market(s)

High Affluence 25-70

Number of Pages Required

5+ page

Font styles to use
Sans Serif
Other font styles liked:
• Muli Fine

Requirements
Must have
• All the current features on the website
• Very elegant
• Main cover image
• Lots of lifestyle imagers - less blank space
• 1. Online Shop
• 2. Home page
• 3. Contact us/enquiry page
• 4. Jewellery Page
• 5. About page

```html
<!DOCTYPE html>
<html lang="en">
<head>
<meta charset="utf-8">
<title>Hollis Fenwick — Finer Jewellery</title>
<link rel="stylesheet" href="https://fonts.googleapis.com/css2?family=Roboto+Condensed:wght@400;700&family=Open+Sans:wght@400;600;700&display=swap">
<style>
:root{
  --black:#0d0d0d;
  --ink:#222;
  --text:#555;
  --gold:#d9b556;
  --white:#fff;
  --line:#d6d6d6;
  --footer:#111;
  --copy-bar:#2a2a2a;
  --head:"Roboto Condensed",sans-serif;
  --body:"Open Sans",sans-serif;
}
*{box-sizing:border-box;margin:0;padding:0}
html,body{width:1200px;height:2335px;overflow:hidden;background:var(--white);font-family:var(--body);color:var(--ink)}
.page{position:relative;width:1200px;height:2335px}
a{color:inherit;text-decoration:none}

/* top bar */
.top-bar{position:absolute;left:0;top:0;width:1200px;height:37px;background:var(--black);color:var(--white);font-size:11px;display:flex;align-items:center;padding:0 200px}
.top-bar .mail{display:flex;align-items:center;gap:8px}
.top-bar .account{margin-left:auto;display:flex;gap:22px}
.top-bar .account span{display:flex;align-items:center;gap:5px}

/* nav */
.main-nav{position:absolute;left:0;top:37px;width:1200px;height:73px;background:var(--white);display:flex;align-items:center;padding:0 200px}
.brand{display:flex;align-items:center;gap:8px;font-family:var(--head);font-size:24px;color:var(--black);letter-spacing:.5px}
.brand .mark{width:34px;height:34px;background:var(--black)}
.menu{margin-left:auto;display:flex;gap:6px;font-size:11px;font-family:var(--body)}
.menu a{padding:8px 9px;color:var(--ink)}
.menu a.active{background:#555;color:var(--white);border-radius:2px}

/* hero */
.hero{position:absolute;left:0;top:110px;width:1200px;height:575px;background:radial-gradient(ellipse at 30% 45%,#e9e2d8 0,#b9a89a 22%,#9a1d24 38%,#3a0f12 65%,#151010 100%);text-align:center;color:var(--white)}
.hero .scrim{position:absolute;inset:0;background:rgba(0,0,0,.25)}
.hero-content{position:absolute;left:0;right:0;top:148px}
.hero .kicker{font-family:var(--head);font-weight:700;font-size:17px;letter-spacing:.5px;margin-top:14px}
.hero .title-wrap{position:relative;width:355px;margin:12px auto 0;padding:14px 0}
.hero .title-wrap::before,.hero .title-wrap::after{content:"";position:absolute;left:0;right:0;height:2px;background:var(--white)}
.hero .title-wrap::before{top:0}.hero .title-wrap::after{bottom:0}
.hero h1{font-family:var(--head);font-weight:700;font-size:48px;letter-spacing:1px;line-height:1}
.hero .lede{font-size:14px;font-weight:600;margin-top:16px}
.btn-dark{display:inline-block;margin-top:38px;background:var(--black);color:var(--white);border:1px solid #888;padding:13px 18px;font-size:13px;font-weight:600}
.arrow{position:absolute;top:306px;width:52px;height:44px;background:var(--white);display:flex;align-items:center;justify-content:center}
.arrow.prev{left:0}.arrow.next{right:0}

/* tiles */
.tile{position:absolute;overflow:hidden;color:var(--white)}
.tile .photo{position:absolute;inset:0}
.tile h2{font-family:var(--head);font-weight:400;font-size:25px;line-height:1.2}
.btn-outline{display:inline-block;border:1px solid var(--white);padding:8px 18px;font-size:11px;font-weight:600;color:var(--white)}
.tile .copy{position:absolute;text-align:center}

.t-browse{left:200px;top:708px;width:335px;height:269px}
.t-browse .photo{background:linear-gradient(90deg,#3a2a25 0,#1a1412 45%,#000 100%)}
.t-browse .copy{left:190px;top:70px;width:130px}
.t-browse .btn-outline{margin-top:16px}

.t-shop{left:552px;top:708px;width:448px;height:269px}
.t-shop .photo{background:linear-gradient(135deg,#9a6b55 0,#d8b9a6 35%,#eadbd1 60%,#c7a28c 100%)}
.t-shop .copy{right:36px;top:35px;width:130px}
.t-shop .btn-outline{margin-top:10px}

.t-welcome{left:200px;top:1000px;width:335px;height:270px;background:var(--gold)}
.t-welcome .copy{left:30px;right:30px;top:38px}
.t-welcome p{font-size:11px;line-height:1.75;margin-top:16px}
.t-welcome .btn-outline{margin-top:16px}

.t-videos{left:552px;top:1000px;width:448px;height:270px;background:var(--black)}
.t-videos .photo{left:190px;background:radial-gradient(ellipse at 55% 50%,#d9d9d9 0,#8a8a8a 30%,#2a2a2a 60%,#000 80%)}
.t-videos .copy{left:28px;top:38px;text-align:left}
.t-videos .btn-outline{margin-top:10px}
.play{position:absolute;left:205px;top:117px;width:36px;height:36px;border-radius:50%;background:#e03a3a}

.story{position:absolute;left:200px;top:1295px;width:800px;height:317px;border:1px solid var(--line);background:var(--white)}
.story .photo{position:absolute;left:0;top:0;width:300px;height:315px;background:linear-gradient(90deg,#7a4a30 0,#c79a7a 40%,#f1e4da 80%,#fff 100%)}
.story .body{position:absolute;left:322px;top:42px;width:440px}
.story h2{font-family:var(--head);font-weight:400;font-size:25px;color:var(--ink);border-left:2px solid var(--ink);padding:4px 0 4px 8px}
.story p{font-size:11px;line-height:1.95;color:var(--text);margin-top:22px}
.btn-line{display:inline-block;margin-top:22px;border:1px solid var(--ink);border-radius:2px;padding:9px 28px;font-size:11px;font-weight:600;color:var(--ink)}

.t-aurelle{left:200px;top:1637px;width:335px;height:269px}
.t-aurelle .photo{background:radial-gradient(ellipse at 50% 55%,#8c7a70 0,#5b4438 45%,#3a2a22 100%)}
.t-aurelle .copy{left:0;right:0;top:100px}
.t-aurelle .btn-outline{margin-top:4px}

.t-diamonds{left:552px;top:1637px;width:448px;height:269px}
.t-diamonds .photo{background:radial-gradient(ellipse at 50% 55%,#e03030 0,#b51b1b 30%,#c9c2c0 60%,#e8e4e2 100%)}
.t-diamonds .copy{left:0;right:0;top:83px}
.t-diamonds .btn-outline{margin-top:8px;padding:8px 30px}

/* newsletter */
.newsletter{position:absolute;left:0;top:1931px;width:1200px;height:84px;background:var(--gold);display:flex;align-items:center;padding:0 200px;color:var(--white)}
.newsletter .intro{margin-left:22px}
.newsletter h3{font-family:var(--head);font-weight:400;font-size:24px}
.newsletter h3 b{color:var(--black);font-weight:400}
.newsletter small{font-size:11px;font-style:italic}
.subscribe{margin-left:auto;display:flex}
.subscribe .field{width:296px;height:34px;background:var(--white);color:#666;font-size:11px;display:flex;align-items:center;padding-left:16px}
.subscribe .go{width:46px;height:34px;background:var(--black);display:flex;align-items:center;justify-content:center}

/* footer */
.site-footer{position:absolute;left:0;top:2015px;width:1200px;height:280px;background:var(--footer);color:var(--white)}
.site-footer h4{font-family:var(--head);font-weight:400;font-size:16px;padding-bottom:8px;border-bottom:1px solid #333}
.col{position:absolute;top:40px}
.col-about{left:200px;width:280px}
.col-about h4{display:flex;align-items:center;gap:10px;font-size:18px;border:none}
.col-about p{font-size:11px;line-height:2.2;margin-top:8px;padding-bottom:10px;border-bottom:1px solid #333}
.follow{display:flex;align-items:center;gap:14px;margin-top:14px;font-family:var(--head);font-size:14px}
.follow i{width:9px;height:9px;border-radius:50%;background:var(--white);display:inline-block}
.col-nav{left:541px;width:120px}
.col-nav ul{list-style:none;font-size:11px;line-height:26px;margin-top:8px}
.col-contact{left:703px;width:297px}
.col-contact li{list-style:none;display:flex;gap:18px;font-size:11px;line-height:1.75;margin-top:14px}
.col-contact svg{flex:none;margin-top:2px}
.copyright{position:absolute;left:0;top:2295px;width:1200px;height:40px;background:var(--copy-bar);color:#bbb;font-size:11px;display:flex;align-items:center;justify-content:center}
</style>
</head>
<body>
<div class="page">

  <div class="top-bar">
    <span class="mail"><svg width="14" height="10" viewBox="0 0 14 10"><rect x=".5" y=".5" width="13" height="9" fill="#fff"/><path d="M1 1l6 5 6-5" stroke="#000" fill="none"/></svg>info@hollisfenwick.com</span>
    <div class="account">
      <span><svg width="9" height="11" viewBox="0 0 9 11"><rect y="5" width="9" height="6" fill="#fff"/><path d="M2 5V3a2.5 2.5 0 015 0v2" stroke="#fff" fill="none" stroke-width="1.4"/></svg>Sign In</span>
      <span><svg width="11" height="11" viewBox="0 0 11 11"><circle cx="7.5" cy="3.5" r="3" fill="#fff"/><path d="M6 5L1 10" stroke="#fff" stroke-width="2"/></svg>Register</span>
      <span><svg width="12" height="11" viewBox="0 0 12 11"><path d="M6 10.5L1 5.5A2.8 2.8 0 016 1.8 2.8 2.8 0 0111 5.5z" fill="#fff"/></svg>Wishlist</span>
      <span><svg width="16" height="12" viewBox="0 0 16 12"><path d="M0 1h3l2 7h8l2-5H4" stroke="#fff" fill="none" stroke-width="1.4"/><circle cx="6" cy="10.5" r="1.3" fill="#fff"/><circle cx="12" cy="10.5" r="1.3" fill="#fff"/></svg>My Cart 0</span>
    </div>
  </div>

  <header class="main-nav">
    <div class="brand"><span class="mark"></span>Hollis Fenwick</div>
    <nav class="menu">
      <a class="active" href="#">Browse Collection</a>
      <a href="#">Videos</a>
      <a href="#">Online Shop</a>
      <a href="#">About Our Diamonds</a>
      <a href="#">History of HF</a>
      <a href="#">Contact Us</a>
    </nav>
  </header>

  <section class="hero" role="img" aria-label="Diamond ring in an open red jewellery box beside a red rose">
    <div class="scrim"></div>
    <div class="hero-content">
      <svg width="54" height="38" viewBox="0 0 54 38"><path d="M12 2h30l10 11-25 23L2 13z M2 13h50 M12 2l7 11 8 23 8-23 7-11 M19 13l8-11 8 11" fill="none" stroke="#fff" stroke-width="2"/></svg>
      <div class="kicker">FINER JEWELLERY SINCE 1923</div>
      <div class="title-wrap"><h1>HOLLIS FENWICK</h1></div>
      <p class="lede">Hollis Fenwick are Australia's premier fine jewellery designers and diamond specialists</p>
      <a class="btn-dark" href="#">View Collection</a>
    </div>
    <span class="arrow prev"><svg width="20" height="12" viewBox="0 0 20 12"><path d="M19 6H2M7 1L2 6l5 5" stroke="#000" stroke-width="2.4" fill="none"/></svg></span>
    <span class="arrow next"><svg width="20" height="12" viewBox="0 0 20 12"><path d="M1 6h17M13 1l5 5-5 5" stroke="#000" stroke-width="2.4" fill="none"/></svg></span>
  </section>

  <article class="tile t-browse">
    <div class="photo" role="img" aria-label="Woman wearing a diamond necklace and drop earrings"></div>
    <div class="copy"><h2>Browse Collection</h2><a class="btn-outline" href="#">View Collecton</a></div>
  </article>

  <article class="tile t-shop">
    <div class="photo" role="img" aria-label="Hands of a couple, one wearing a diamond engagement ring"></div>
    <div class="copy"><h2>Online Shop</h2><a class="btn-outline" href="#">View Collecton</a></div>
  </article>

  <article class="tile t-welcome">
    <div class="copy">
      <h2>Welcome to Hollis Fenwick</h2>
      <p>Hollis Fenwick are Australia's premier fine jewellery designers and diamond specialists, featuring an exclusive range of quality jewellery plus an expert made-to-order service.</p>
      <a class="btn-outline" href="#">View Collecton</a>
    </div>
  </article>

  <article class="tile t-videos">
    <div class="photo" role="img" aria-label="Close-up of a princess cut diamond ring with pavé band"></div>
    <span class="play"><svg width="36" height="36" viewBox="0 0 36 36"><path d="M14 11l12 7-12 7z" fill="#fff"/></svg></span>
    <div class="copy"><h2>Videos</h2><a class="btn-outline" href="#">View More</a></div>
  </article>

  <section class="story">
    <div class="photo" role="img" aria-label="Woman wearing long diamond chandelier earrings"></div>
    <div class="body">
      <h2>The Hollis Fenwick Story</h2>
      <p>Our origins reach back to pre-war France, where in 1923, Hollis Fenwick founded his workrooms in a small studio in Metz. After crafting the finest bespoke jewellery of the region Hollis gained an enthusiastic and appreciative clientele. This success enabled Hollis to relocate the workrooms to Paris, where he was joined by his brother Edmund.</p>
      <a class="btn-line" href="#">Read More</a>
    </div>
  </section>

  <article class="tile t-aurelle">
    <div class="photo" role="img" aria-label="Ornate dark diamond collar necklace worn at the neckline"></div>
    <div class="copy"><h2>Aurelle Diamond</h2><a class="btn-outline" href="#">View Collecton</a></div>
  </article>

  <article class="tile t-diamonds">
    <div class="photo" role="img" aria-label="Diamond ring set in a red velvet ring box"></div>
    <div class="copy"><h2>About Our Diamonds</h2><a class="btn-outline" href="#">Read More</a></div>
  </article>

  <section class="newsletter">
    <svg width="32" height="24" viewBox="0 0 32 24"><rect x="1" y="1" width="30" height="22" fill="none" stroke="#fff" stroke-width="2"/><path d="M1 1l15 12L31 1M1 23l11-10M31 23L20 13" fill="none" stroke="#fff" stroke-width="2"/></svg>
    <div class="intro">
      <h3>Subscribe <b>Newsletter</b></h3>
      <small>Get All Latest News and Offer by Subscribing to Our Newsletter</small>
    </div>
    <div class="subscribe">
      <span class="field">Your E-mail Address</span>
      <span class="go"><svg width="10" height="14" viewBox="0 0 10 14"><path d="M2 1l6 6-6 6" stroke="#fff" stroke-width="2.4" fill="none"/></svg></span>
    </div>
  </section>

  <footer class="site-footer">
    <div class="col col-about">
      <h4><svg width="22" height="16" viewBox="0 0 54 38"><path d="M12 2h30l10 11-25 23L2 13z M2 13h50 M19 13l8-11 8 11" fill="none" stroke="#fff" stroke-width="4"/></svg>Hollis Fenwick</h4>
      <p>Steeped in tradition for almost a century, the ethos of Hollis Fenwick spans three generations to present some of the most beautiful diamond jewellery made in Australia. Our design philosophy conforms ...</p>
      <div class="follow">Follow Us <i></i><i></i><i></i><i></i></div>
    </div>
    <div class="col col-nav">
      <h4>Navigation</h4>
      <ul>
        <li>Browse Collection</li><li>Videos</li><li>Online Shop</li><li>About Our Diamonds</li><li>History of HF</li><li>Contact Us</li>
      </ul>
    </div>
    <div class="col col-contact">
      <h4>Get in Touch</h4>
      <ul>
        <li><svg width="12" height="15" viewBox="0 0 12 15"><path d="M6 14S1 8.5 1 5.5a5 5 0 0110 0C11 8.5 6 14 6 14z" fill="#d9b556"/><circle cx="6" cy="5.5" r="2" fill="#111"/></svg>Hollis Fenwick Jewellers - Lindel Street 208 Lindel Street Melbourne, Victoria 3000</li>
        <li><svg width="13" height="13" viewBox="0 0 13 13"><path d="M3 1l2 3-1.5 1.5a7 7 0 004 4L9 8l3 2-1.5 2.5C5 12 1 8 .5 2.5z" fill="#d9b556"/></svg>(03) 9000 4127</li>
        <li><svg width="14" height="10" viewBox="0 0 14 10"><rect x=".5" y=".5" width="13" height="9" fill="none" stroke="#d9b556"/><path d="M1 1l6 5 6-5" stroke="#d9b556" fill="none"/></svg>info@hollisfenwick.com.au</li>
      </ul>
    </div>
  </footer>
  <div class="copyright">© Copyright 2017 Hollis Fenwick. All Rights Reserved.</div>

</div>
</body>
</html>
```